Brightmoor Glowing - Two Pages of Information and Pictures

We need a two page summary of the Service Offerings of Brightmoor Glowing - a company that installs LED Lighting. We've written the copy and picked images and chart that we like and have laid it out a word document.

We're looking for someone to design a more professional page layout than the generic Word Template. Please do not feel the current layout is suggested. It is only laid out this way because Word had that template. Be as creative as you want.

We would like the images and text to be in the same order that it is in now.

We're also in a rush so speed is appreciated. THANK YOU !!

Target Market(s)

Corporate Offices in New York

Industry/Entity Type

Lighting Fixture

Colors
85cae6
87cfc7
9bcb3c
3377b5

Requirements
Must have
• Must include two pages of the copy and images written and provided in the word document that was uploaded. Must use the Brightmoor colors in the logo.
Nice to have
• An easy to read flow of images and.

```html
<!DOCTYPE html>
<html lang="en">
<head>
<meta charset="utf-8">
<title>Brightmoor Glowing – Service Overview</title>
<link href="https://fonts.googleapis.com/css2?family=Open+Sans:wght@400;600;700&display=swap" rel="stylesheet">
<style>
  :root{
    --backdrop:#e4e4e4;
    --paper:#ffffff;
    --ink:#3a3a3a;
    --heading-green:#6b8f6e;
    --panel-dark:#414042;
    --panel-shade:#58585a;
    --lavender:#b4c3de;
    --teal-light:#b6dcd5;
    --teal-mid:#7ba9b7;
    --bar-service:#a3d6cf;
    --bar-savings:#8fc06d;
    --line-total:#9a9a9a;
    --grid:#e3e3e3;
  }
  *{box-sizing:border-box;margin:0;padding:0}
  html,body{width:975px;height:1200px;overflow:hidden}
  body{background:var(--backdrop);font-family:"Open Sans",Arial,sans-serif;color:var(--ink);position:relative}
  .page{position:absolute;left:83px;top:76px;width:809px;height:1046px;background:var(--paper);overflow:hidden}
  .page-art{position:absolute;left:0;top:0;width:809px;height:1046px}
  .main-column{position:absolute;left:47px;top:88px;width:430px;font-size:11.6px;line-height:15.9px;text-align:justify}
  .section-title{font-size:19px;font-weight:700;color:var(--heading-green);line-height:22px;margin-bottom:3px;text-align:left}
  .main-column p{margin-bottom:15.9px}
  .section-title.second{margin-top:24px}
  .savings-chart{float:right;width:305px;height:203px;margin:4px 0 6px 10px;border:1px solid #cfcfcf;background:#fff}
  .savings-chart svg{display:block}
  .testimonials{position:absolute;left:547px;top:80px;width:215px;color:#fff;font-size:12.4px;line-height:15.9px}
  .testimonials h2{font-size:16.5px;font-weight:700;margin-bottom:14px}
  .quote{margin-bottom:17px;text-align:justify}
  .quote-mark{float:left;font-size:54px;line-height:40px;font-weight:700;margin:2px 8px 0 0;height:30px;font-family:Georgia,serif}
  .quote cite{display:block;text-align:right;font-style:normal;font-weight:700;font-size:12.6px;line-height:16px}
  .brand{position:absolute;left:50px;top:826px;display:flex;align-items:center;gap:10px}
  .brand-dot{width:14px;height:14px;border-radius:50%;background:var(--heading-green)}
  .brand-name{font-size:17px;font-weight:400;letter-spacing:1.5px;color:var(--heading-green)}
  .contact{position:absolute;left:47px;top:937px;font-size:12.6px;font-weight:700;line-height:25.5px;color:#222}
</style>
</head>
<body>
<div class="page">
  <svg class="page-art" viewBox="83 76 809 1046" aria-hidden="false">
    <polygon points="599,76 892,76 892,632 599,797" fill="var(--panel-dark)"/>
    <polygon points="599,650 750,715 599,797" fill="var(--panel-shade)"/>
    <polygon points="745,735 892,655 892,815" fill="var(--lavender)"/>
    <defs>
      <linearGradient id="teamTone" x1="0" y1="0" x2="1" y2="1">
        <stop offset="0" stop-color="#8a6a55"/><stop offset="0.5" stop-color="#5d6f93"/><stop offset="1" stop-color="#7a8aa8"/>
      </linearGradient>
      <linearGradient id="roomTone" x1="0" y1="0" x2="1" y2="1">
        <stop offset="0" stop-color="#6b4a33"/><stop offset="1" stop-color="#c9a27a"/>
      </linearGradient>
      <linearGradient id="lampTone" x1="0" y1="0" x2="1" y2="1">
        <stop offset="0" stop-color="#4a3b2e"/><stop offset="1" stop-color="#d9b27a"/>
      </linearGradient>
    </defs>
    <polygon role="img" aria-label="Photo of the installation team at work, wearing branded shirts" points="458,880 745,742 892,820 892,1000 745,1065 600,990" fill="url(#teamTone)"/>
    <polygon role="img" aria-label="Photo of an office lit with new LED fixtures" points="300,1000 440,905 592,988 440,1082" fill="url(#roomTone)"/>
    <polygon points="440,1122 592,1000 700,1122" fill="var(--teal-light)"/>
    <polygon points="592,1000 745,1070 700,1122" fill="var(--teal-mid)"/>
    <polygon points="700,1122 745,1070 800,1122" fill="var(--lavender)"/>
    <polygon role="img" aria-label="Photo of pendant filament bulbs" points="745,1070 892,1000 892,1122 800,1122" fill="url(#lampTone)"/>
  </svg>

  <div class="main-column">
    <h2 class="section-title">Why use Brightmoor?</h2>
    <p>Brightmoor’s customers understand the value of LEDs but don’t want to deal with the risk, hassle and capital cost on their own. Brightmoor starts saving customers money the first month – typically a net-savings of about 4.7 cents a square-foot per month.
      <span class="savings-chart">
        <svg width="303" height="201" viewBox="0 0 304 203" role="img" aria-label="Chart of annual and total net-savings over ten years">
          <text x="152" y="20" font-size="8.5" text-anchor="middle" fill="#444" font-family="Open Sans,sans-serif" font-weight="600">Annual and Total Net-Savings of 250,000 ft2 Customer</text>
          <g stroke="var(--grid)" stroke-width="0.7">
            <line x1="34" y1="32" x2="268" y2="32"/><line x1="34" y1="54.3" x2="268" y2="54.3"/><line x1="34" y1="76.7" x2="268" y2="76.7"/><line x1="34" y1="99" x2="268" y2="99"/><line x1="34" y1="121.3" x2="268" y2="121.3"/><line x1="34" y1="143.7" x2="268" y2="143.7"/><line x1="34" y1="166" x2="268" y2="166"/>
          </g>
          <g font-size="5.5" fill="#555" font-family="Open Sans,sans-serif" text-anchor="end">
            <text x="30" y="34">$300</text><text x="30" y="56">$250</text><text x="30" y="79">$200</text><text x="30" y="101">$150</text><text x="30" y="123">$100</text><text x="30" y="146">$50</text><text x="30" y="168">$-</text>
          </g>
          <g font-size="5.5" fill="#555" font-family="Open Sans,sans-serif">
            <text x="272" y="34">$2.0</text><text x="272" y="47">$1.8</text><text x="272" y="61">$1.6</text><text x="272" y="74">$1.4</text><text x="272" y="88">$1.2</text><text x="272" y="101">$1.0</text><text x="272" y="114">$0.8</text><text x="272" y="128">$0.6</text><text x="272" y="141">$0.4</text><text x="272" y="155">$0.2</text><text x="272" y="168">$0.0</text>
          </g>
          <text x="12" y="60" font-size="5" fill="#555" transform="rotate(-90 12 60)">Thousands</text>
          <text x="298" y="50" font-size="5" fill="#555" transform="rotate(90 298 50)">Millions</text>
          <g fill="var(--bar-service)">
            <rect x="35.7" y="121.3" width="9" height="44.7"/><rect x="59.1" y="121.3" width="9" height="44.7"/><rect x="82.5" y="121.3" width="9" height="44.7"/><rect x="105.9" y="121.3" width="9" height="44.7"/><rect x="129.3" y="121.3" width="9" height="44.7"/>
          </g>
          <g fill="var(--bar-savings)">
            <rect x="44.7" y="103.4" width="9" height="62.6"/><rect x="68.1" y="103.4" width="9" height="62.6"/><rect x="91.5" y="103.4" width="9" height="62.6"/><rect x="114.9" y="103.4" width="9" height="62.6"/><rect x="138.3" y="103.4" width="9" height="62.6"/>
            <rect x="161.7" y="58.8" width="9" height="107.2"/><rect x="185.1" y="58.8" width="9" height="107.2"/><rect x="208.5" y="58.8" width="9" height="107.2"/><rect x="231.9" y="58.8" width="9" height="107.2"/><rect x="255.3" y="58.8" width="9" height="107.2"/>
          </g>
          <polyline fill="none" stroke="var(--line-total)" stroke-width="1.2" points="45.7,156.6 69.1,147.2 92.5,137.9 115.9,128.5 139.3,119.1 162.7,103 186.1,86.9 209.5,70.9 232.9,54.8 256.3,38.7"/>
          <g font-size="5.5" fill="#555" text-anchor="middle" font-family="Open Sans,sans-serif">
            <text x="45.7" y="175">1</text><text x="69.1" y="175">2</text><text x="92.5" y="175">3</text><text x="115.9" y="175">4</text><text x="139.3" y="175">5</text><text x="162.7" y="175">6</text><text x="186.1" y="175">7</text><text x="209.5" y="175">8</text><text x="232.9" y="175">9</text><text x="256.3" y="175">10</text>
          </g>
          <g font-size="5" fill="#555" font-family="Open Sans,sans-serif">
            <rect x="52" y="185" width="9" height="4" fill="var(--bar-service)"/><text x="64" y="189">Annual Brightmoor Service</text>
            <rect x="133" y="185" width="9" height="4" fill="var(--bar-savings)"/><text x="145" y="189">Annual Net-Savings</text>
            <line x1="200" y1="187" x2="210" y2="187" stroke="var(--line-total)"/><text x="213" y="189">Total Net-Savings</text>
          </g>
        </svg>
      </span>
      Brightmoor will design aesthetic LED systems and install the best available technology.</p>
    <p>Brightmoor provides LEDs at the best cost with its as-a-service structure, which puts the cost of lighting into clients’ monthly operating budget for less than they save. By installing projects immediately, Brightmoor eliminates the cost of foregone savings that would accumulate from delayed implementation.</p>
    <p>It can be risky to adopt new technology, especially when salespeople try to sell more than is needed. Brightmoor has access to better equipment and at better cost than is widely available on the open market and passes that quality and savings on to its customers. Brightmoor guarantees performance for 5 years, which removes the risk of a failed project.</p>
    <h2 class="section-title second">The Best Team in LEDs</h2>
    <p>Brightmoor is a team of lighting experts who get the evolution of lighting and efficiency. Simply put, we come in up every day with one goal: to provide an excellent service that saves money and uses less electricity. Part of the team focuses on the supply chain of the very best equipment that customers have come to appreciate. Part of the team focuses on the project management of each installation. And, part of the team focuses on resolving any questions customers might have in their transition. Together we make up the best team in LEDs and work tirelessly to make it easy to upgrade.</p>
  </div>

  <section class="testimonials">
    <h2>Testimonials</h2>
    <blockquote class="quote"><span class="quote-mark">“</span>Brightmoor made a huge improvement in the lighting for our headquarters. The installation process was as smooth as can be and the service since has been excellent.”<cite>– Harbor Health</cite></blockquote>
    <blockquote class="quote"><span class="quote-mark">“</span>In a museum, quality lighting is paramount. Brightmoor has been a great partner in helping us transition to LEDs that look great, save us money, and make lighting management so much simpler.”<cite>– Youth Gallery of Art,<br>New York</cite></blockquote>
    <blockquote class="quote"><span class="quote-mark">“</span>We are so happy to have had Brightmoor’s help building out our new office space – they put their lighting expertise to work delivering beautiful LEDs and fixtures. It was cost-effective, removed lighting from the build-out budget, and it’s been a joy to work with them since.”<cite>– Loomcraft, Inc</cite></blockquote>
  </section>

  <div class="brand"><span class="brand-dot"></span><span class="brand-name">BRIGHTMOOR</span></div>

  <address class="contact" style="font-style:normal">
    Phone: 347 555 GLOW<br>
    Website: brightmoorglowing.com<br>
    Email: info@brightmoorglowing.com
  </address>
</div>
</body>
</html>
```